Railroad Association needs One-Page Infographic

Please see attachment for text and graphic. email with questions please. This piece will be handed out to legislators and state officials.

Target Market(s)

state legislature. state officials

Font styles to use
Serif

Colors
ec1f27

Requirements
Must have
• The graphic needs to be done right. Please email me with any questions.

```html
<!DOCTYPE html>
<html lang="en">
<head>
<meta charset="utf-8">
<title>Crossing Railroad Right of Way (ROW)</title>
<link rel="stylesheet" href="https://fonts.googleapis.com/css2?family=Arimo:wght@400;500;700&display=swap">
<style>
  :root {
    --sky: #2aa3dc;
    --navy: #0f1d40;
    --ink: #1b1b1b;
    --red: #ec1f27;
    --white: #ffffff;
    --green: #6aab2b;
    --blue: #1d86c8;
    --orange: #f5a132;
    --peach: #fdc98b;
  }
  * { box-sizing: border-box; margin: 0; padding: 0; }
  html, body { width: 851px; height: 1200px; overflow: hidden; }
  body { font-family: "Arimo", Arial, sans-serif; color: var(--ink); background: var(--white); }

  .sheet { position: relative; width: 851px; height: 1200px; overflow: hidden; }

  .hero { position: absolute; left: 0; top: 0; width: 851px; height: 721px; background: var(--sky); }
  .hero-strip { position: absolute; left: 0; top: 0; width: 100%; height: 8px; background: var(--navy); }
  .hero-title { position: absolute; top: 24px; width: 100%; text-align: center; font-size: 34px; font-weight: 500; color: #111; }
  .hero-subtitle { position: absolute; top: 64px; width: 100%; text-align: center; font-size: 29px; font-weight: 400; color: #111; }

  .hero-illustration { position: absolute; left: 380px; top: 118px; width: 440px; height: 250px; border-radius: 14px;
    background: linear-gradient(160deg, #555 0%, #c81a22 45%, #e3242c 70%, #555 100%); opacity: .9; }

  .process-heading { position: absolute; left: 22px; top: 284px; display: flex; align-items: center; gap: 8px; }
  .process-heading .rule { width: 62px; height: 2px; background: var(--navy); position: relative; }
  .process-heading .rule::before { content: ""; position: absolute; top: -3px; width: 6px; height: 6px; border: 1.5px solid var(--navy); border-radius: 50%; background: var(--sky); }
  .process-heading .rule.left::before { left: -4px; }
  .process-heading .rule.right::before { right: -4px; }
  .process-heading h2 { font-size: 32px; font-weight: 500; color: var(--navy); letter-spacing: .5px; }

  .step { position: absolute; left: 0; height: 84px; }
  .step svg { position: absolute; left: 0; top: 0; }
  .step-number { position: absolute; left: 0; top: 0; width: 62px; height: 84px; display: flex; align-items: center; justify-content: center; font-size: 38px; font-weight: 500; color: #111; }
  .step-text { position: absolute; left: 72px; top: 50%; transform: translateY(-50%); font-size: 15.5px; font-weight: 700; line-height: 1.3; color: #111; white-space: nowrap; }

  .keys { position: absolute; left: 0; top: 721px; width: 851px; height: 479px; background: var(--red); }
  .keys-title { position: absolute; left: 26px; top: 40px; font-size: 20px; font-weight: 700; color: var(--white); }
  .key { position: absolute; width: 150px; text-align: center; }
  .key-icon { width: 76px; height: 76px; margin: 0 auto; border-radius: 50%; background: var(--navy); display: flex; align-items: center; justify-content: center; }
  .key-label { margin-top: 12px; font-size: 16px; color: var(--white); }

  .seal { position: absolute; left: 535px; top: 743px; width: 302px; height: 302px; border-radius: 50%; background: var(--navy); display: flex; align-items: center; justify-content: center; }
  .seal-ring { width: 258px; height: 258px; border-radius: 50%; background: var(--red); display: flex; align-items: center; justify-content: center; }
  .seal-core { width: 246px; height: 246px; border-radius: 50%; background: var(--white); display: flex; align-items: center; justify-content: center; text-align: center; padding: 0 42px; font-size: 16px; font-weight: 700; line-height: 1.25; color: #111; }

  .brand { position: absolute; left: 30px; top: 1090px; width: 104px; height: 84px; background: var(--white); display: flex; flex-direction: column; align-items: center; justify-content: center; gap: 6px; }
  .brand-mark { width: 12px; height: 12px; background: var(--navy); }
  .brand-name { font-size: 11px; font-weight: 700; color: var(--navy); line-height: 1.2; text-align: center; }
  .quote { position: absolute; left: 168px; top: 1093px; width: 664px; font-size: 15px; line-height: 1.3; color: var(--white); }
</style>
</head>
<body>
<div class="sheet">
  <section class="hero">
    <div class="hero-strip"></div>
    <h1 class="hero-title">Crossing Railroad Right of Way (ROW)</h1>
    <p class="hero-subtitle">What is the process?</p>
    <div class="hero-illustration" role="img" aria-label="Illustration of a red passenger train crossing a winding road"></div>

    <div class="process-heading">
      <span class="rule left"></span><h2>PROCESS</h2><span class="rule right"></span>
    </div>

    <div class="step" style="top:356px;width:495px">
      <svg width="495" height="84"><path d="M0 0H380Q495 10 495 60V84H0Z" fill="var(--green)"/><rect x="0" y="0" width="62" height="84" rx="10" fill="var(--blue)"/></svg>
      <span class="step-number">1</span>
      <p class="step-text">Contact railroad to obtain<br>application and specifications.</p>
    </div>
    <div class="step" style="top:445px;width:575px">
      <svg width="575" height="84"><path d="M0 0H460Q575 10 575 60V84H0Z" fill="var(--blue)"/><rect x="0" y="0" width="62" height="84" rx="10" fill="var(--green)"/></svg>
      <span class="step-number">2</span>
      <p class="step-text">Submit application to<br>railroad with engineering plans.</p>
    </div>
    <div class="step" style="top:533px;width:650px">
      <svg width="650" height="84"><path d="M0 0H535Q650 10 650 60V84H0Z" fill="var(--orange)"/><rect x="0" y="0" width="62" height="84" rx="10" fill="var(--peach)"/></svg>
      <span class="step-number">3</span>
      <p class="step-text">When plans are approved, enter<br>into license agreement with railroad.</p>
    </div>
    <div class="step" style="top:621px;width:728px">
      <svg width="728" height="84"><path d="M0 0H613Q728 10 728 60V84H0Z" fill="var(--peach)"/><rect x="0" y="0" width="62" height="84" rx="10" fill="var(--orange)"/></svg>
      <span class="step-number">4</span>
      <p class="step-text">With railroad safety protocols and approved work plan<br>in place, coordinate with operations to obtain flagman.</p>
    </div>
  </section>

  <section class="keys">
    <h3 class="keys-title">Keys to a SAFE and thorough process:</h3>

    <div class="key" style="left:3px;top:83px">
      <div class="key-icon"><svg width="40" height="40" viewBox="0 0 40 40"><rect x="4" y="6" width="32" height="30" rx="3" fill="none" stroke="#fff" stroke-width="2.5"/><line x1="4" y1="13" x2="36" y2="13" stroke="#fff" stroke-width="2.5"/><path d="M12 24l6 6 11-12" fill="none" stroke="#fff" stroke-width="3"/></svg></div>
      <p class="key-label">Plan</p>
    </div>
    <div class="key" style="left:153px;top:83px">
      <div class="key-icon"><svg width="40" height="40" viewBox="0 0 40 40"><circle cx="17" cy="17" r="11" fill="none" stroke="#fff" stroke-width="2.5"/><line x1="25" y1="25" x2="35" y2="35" stroke="#fff" stroke-width="3.5"/></svg></div>
      <p class="key-label">Review</p>
    </div>
    <div class="key" style="left:302px;top:83px">
      <div class="key-icon"><svg width="40" height="40" viewBox="0 0 40 40"><rect x="4" y="8" width="22" height="15" rx="3" fill="#fff"/><path d="M8 23v6l6-6z" fill="#fff"/><rect x="16" y="18" width="20" height="13" rx="3" fill="none" stroke="#fff" stroke-width="2"/></svg></div>
      <p class="key-label">Communicate</p>
    </div>
    <div class="key" style="left:77px;top:208px">
      <div class="key-icon"><svg width="40" height="40" viewBox="0 0 40 40"><rect x="5" y="18" width="7" height="16" fill="none" stroke="#fff" stroke-width="2.5"/><path d="M12 20l7-12q3 0 3 4l-1 6h11q3 0 2 4l-3 10q-1 2-3 2H12" fill="none" stroke="#fff" stroke-width="2.5"/></svg></div>
      <p class="key-label">Agree</p>
    </div>
    <div class="key" style="left:227px;top:208px">
      <div class="key-icon"><svg width="40" height="40" viewBox="0 0 40 40"><path d="M16 5h8v13h7l-11 11-11-11h7z" fill="#fff"/><path d="M5 27v7h30v-7" fill="none" stroke="#fff" stroke-width="3"/></svg></div>
      <p class="key-label">Install</p>
    </div>
  </section>

  <div class="seal"><div class="seal-ring"><p class="seal-core">Every railroad company has a detailed process to ensure SAFETY and avoid interuption to operations when crossing railroad ROW</p></div></div>

  <div class="brand"><span class="brand-mark"></span><span class="brand-name">Lakeshore Rail<br>Association</span></div>
  <p class="quote">"Railroads adhere to strict safety and notification standards so that both the entity creating an incumbrance on railroad property as well as the railroads themselves, establish clear rules of engagement that allow each to accomplish their own goals while minimizing risk to the public"</p>
</div>
</body>
</html>
```